Wheels Open Doors - Two sided invitation to encourage bike friendly businesses

Pedal Haven is a charitable trust who want to grow everyday bike use. One way to do that is help businesses understand that 'Wheels Open Doors'. We want a postcard sized 'invitation' that bike users can give to their favourite businesses, inviting them to find out more about all the benefits of attracting bike users to their business and becoming a 'Pedal Haven Business'. We are currently finalising copy, so the attached is indicative but not final copy. The docx file is the words, the png is indicative of the type of infographic we might want to feature.
I'm also attaching a mock up of our window sticker for businesses, and some social shares featuring photographic images which we have available to use. This will give you an idea of our branding to date. Our extended branding concept (which we will use when we re-do our website) is based on icons, so I'm open to seeing icon focused designs also.
The feel needs to be inviting, credible, enticing, business like, noticeable, with a strong call to action.

Target Market(s)

Small business operators: retail, cafes, etc; also managers of larger chains such as supermarkets, gyms, etc.

Industry/Entity Type

Non Profit

Font styles to use
Serif
Other font styles liked:
• Logo is done in Raleway, so need compatible font.

Colors
9ccb3b

Requirements
Must have
• Two Sides
• Use the copy provided
• Strong call to action - visiting website
• Use our colours
• A6 sized cards
Nice to have
• Compelling images and/or infographic
• Consistency with circles / curves used in other branding.
Should not have
• Not bland, not something that will get lost on the recipients desk or counter.

```html
<!DOCTYPE html>
<html lang="en">
<head>
<meta charset="utf-8">
<title>Pedal Haven – Invitation Card</title>
<link rel="stylesheet" href="https://fonts.googleapis.com/css2?family=Bebas+Neue&family=Baloo+2:wght@700&family=Fira+Sans+Condensed:wght@500;600&family=Raleway:wght@500&display=swap">
<style>
  :root {
    --canvas: #949598;
    --lime: #9ccb3b;
    --lime-light: #aed34f;
    --green: #12a14b;
    --green-deep: #0e8f40;
    --yellow: #d6e021;
    --tan: #b7a57a;
    --white: #ffffff;
  }
  html, body { margin: 0; padding: 0; overflow: hidden; }
  body { width: 1200px; height: 1200px; background: var(--canvas); position: relative; }
  .card { position: absolute; width: 474px; height: 697px; display: block; }
  .card--front { left: 67px; top: 221px; }
  .card--back { left: 663px; top: 224px; }
  .caps { font-family: "Bebas Neue", sans-serif; }
  .body { font-family: "Fira Sans Condensed", sans-serif; font-weight: 600; }
  .display { font-family: "Baloo 2", sans-serif; font-weight: 700; }
  .brand { font-family: "Raleway", sans-serif; font-weight: 500; }
</style>
</head>
<body>

<!-- Front side -->
<svg class="card card--front" viewBox="0 0 592 871" xmlns="http://www.w3.org/2000/svg">
  <defs>
    <clipPath id="front-clip"><rect width="592" height="871"/></clipPath>
    <linearGradient id="street-tone" x1="0" y1="0" x2="1" y2="1">
      <stop offset="0" stop-color="#8a7f7a"/><stop offset="0.5" stop-color="#b28a8e"/><stop offset="1" stop-color="#6f6a66"/>
    </linearGradient>
    <linearGradient id="cafe-tone" x1="0" y1="0" x2="1" y2="1">
      <stop offset="0" stop-color="#3f6a35"/><stop offset="0.6" stop-color="#7f8b7a"/><stop offset="1" stop-color="#3b3f44"/>
    </linearGradient>
  </defs>
  <g clip-path="url(#front-clip)">
    <rect class="card-bg" width="592" height="871" fill="var(--lime)"/>
    <rect class="top-band" width="592" height="14" fill="var(--green)"/>

    <rect class="skyline" x="0" y="374" width="592" height="240" fill="var(--lime-light)" opacity="0.55" role="img" aria-label="Faint city skyline silhouette"/>

    <circle class="photo-ring" cx="106" cy="264" r="214" fill="var(--green)"/>
    <circle class="photo photo--riders" cx="106" cy="264" r="208" fill="url(#street-tone)" role="img" aria-label="Photo of two smiling cyclists riding down a city street"/>

    <circle class="photo-ring" cx="486" cy="174" r="130" fill="var(--green)"/>
    <circle class="photo photo--cafe" cx="486" cy="174" r="123" fill="url(#cafe-tone)" role="img" aria-label="Photo of friends at a cafe table with bikes parked beside them"/>

    <g class="brand-tag">
      <rect x="200" y="34" width="143" height="57" rx="8" fill="var(--green)"/>
      <circle cx="165" cy="61" r="50" fill="var(--white)" stroke="var(--green)" stroke-width="4"/>
      <text class="brand" x="226" y="58" font-size="22" fill="var(--white)">Pedal</text>
      <text class="brand" x="226" y="82" font-size="22" fill="var(--white)">Haven</text>
    </g>

    <g class="bubble bubble--yellow">
      <circle cx="306" cy="304" r="78" fill="var(--yellow)" opacity="0.85" stroke="var(--green)" stroke-width="2"/>
      <text class="caps" font-size="24" fill="var(--green)" text-anchor="middle">
        <tspan x="304" y="269">They spend</tspan><tspan x="304" y="293">$$$ locally as</tspan><tspan x="304" y="317">they must carry</tspan><tspan x="304" y="341">what they buy.</tspan>
      </text>
    </g>
    <g class="bubble bubble--yellow">
      <circle cx="508" cy="324" r="70" fill="var(--yellow)" opacity="0.85" stroke="var(--green)" stroke-width="2"/>
      <text class="caps" font-size="21" fill="var(--green)" text-anchor="middle">
        <tspan x="508" y="294">Biking</tspan><tspan x="508" y="317">customers</tspan><tspan x="508" y="340">spend $$$ where</tspan><tspan x="508" y="363">parking's easy.</tspan>
      </text>
    </g>
    <g class="bubble bubble--yellow">
      <circle cx="126" cy="509" r="92" fill="var(--yellow)" opacity="0.85" stroke="var(--green)" stroke-width="2"/>
      <text class="caps" font-size="24" fill="var(--green)" text-anchor="middle">
        <tspan x="124" y="459">Biking</tspan><tspan x="124" y="484">customers</tspan><tspan x="124" y="509">move slower,</tspan><tspan x="124" y="534">so see what</tspan><tspan x="124" y="559">your business</tspan><tspan x="124" y="584">offers.</tspan>
      </text>
    </g>

    <g class="headline-disc">
      <circle cx="370" cy="506" r="110" fill="var(--lime-light)" stroke="#c9dfa0" stroke-width="4"/>
      <circle cx="370" cy="506" r="102" fill="var(--green)"/>
      <text class="display" font-size="42" fill="var(--white)" text-anchor="middle">
        <tspan x="370" y="476">Why</tspan><tspan x="370" y="520">welcome</tspan><tspan x="370" y="564">bikes?</tspan>
      </text>
    </g>

    <g class="bubble bubble--green">
      <circle cx="204" cy="722" r="110" fill="var(--green)" stroke="var(--yellow)" stroke-width="3"/>
      <text class="body" font-size="23" fill="var(--yellow)" text-anchor="middle">
        <tspan x="201" y="682">They tell friends</tspan><tspan x="201" y="709">where's good to</tspan><tspan x="201" y="736">park and shop,</tspan><tspan x="201" y="762">where they</tspan><tspan x="201" y="788">feel welcome.</tspan>
      </text>
    </g>
    <g class="bubble bubble--green">
      <circle cx="470" cy="722" r="108" fill="var(--green)" stroke="var(--yellow)" stroke-width="3"/>
      <text class="body" font-size="22" fill="var(--yellow)" text-anchor="middle">
        <tspan x="470" y="667">You're helping</tspan><tspan x="470" y="693">people</tspan><tspan x="470" y="719">environmentally,</tspan><tspan x="470" y="745">budget and heart</tspan><tspan x="470" y="771">friendly – and they'll</tspan><tspan x="470" y="797">you for it.</tspan>
      </text>
    </g>

    <g class="footer">
      <polygon points="36,846 261,846 261,870 20,870 36,858 20,846" fill="var(--yellow)"/>
      <polygon points="274,846 592,846 592,871 261,871 274,858 261,846" fill="var(--green)"/>
      <text class="brand" x="282" y="864" font-size="13" fill="var(--white)">www.pedalhaven.org</text>
      <text class="brand" x="490" y="864" font-size="13" fill="var(--white)">Pedal Haven</text>
    </g>
  </g>
</svg>

<!-- Back side -->
<svg class="card card--back" viewBox="0 0 592 872" xmlns="http://www.w3.org/2000/svg">
  <defs>
    <clipPath id="back-clip"><rect width="592" height="872"/></clipPath>
    <linearGradient id="harbour-tone" x1="0" y1="0" x2="0" y2="1">
      <stop offset="0" stop-color="#b8c4cc"/><stop offset="0.5" stop-color="#6e8aa0"/><stop offset="1" stop-color="#7a7870"/>
    </linearGradient>
    <linearGradient id="sunset-tone" x1="0" y1="0" x2="1" y2="1">
      <stop offset="0" stop-color="#4a5a6a"/><stop offset="0.6" stop-color="#c98a3a"/><stop offset="1" stop-color="#3a2410"/>
    </linearGradient>
  </defs>
  <g clip-path="url(#back-clip)">
    <rect class="card-bg" width="592" height="872" fill="var(--lime)"/>
    <path class="infographic-field" d="M0,0 H564 C560,190 420,360 200,360 C110,360 40,330 0,300 Z" fill="var(--green)"/>

    <path class="art art--bikes" d="M14,110 C60,70 180,60 240,150 C290,230 310,290 290,330 C240,340 140,300 80,230 C40,190 10,150 14,110 Z" fill="var(--lime)" opacity="0.35" role="img" aria-label="Illustration of six bicycles parked in a diagonal row"/>
    <rect class="art art--car" x="322" y="40" width="158" height="86" rx="30" fill="var(--yellow)" opacity="0.9" role="img" aria-label="Illustration of a car seen from the front"/>

    <g class="rate-chips caps" font-size="10" fill="var(--green)" text-anchor="middle">
      <circle cx="143" cy="46" r="20" fill="var(--yellow)"/><text x="143" y="45">$16.20</text><text x="143" y="55">per hour</text>
      <circle cx="176" cy="85" r="20" fill="var(--yellow)"/><text x="176" y="84">$16.20</text><text x="176" y="94">per hour</text>
      <circle cx="211" cy="125" r="20" fill="var(--yellow)"/><text x="211" y="124">$16.20</text><text x="211" y="134">per hour</text>
      <circle cx="240" cy="161" r="20" fill="var(--yellow)"/><text x="240" y="160">$16.20</text><text x="240" y="170">per hour</text>
      <circle cx="273" cy="205" r="20" fill="var(--yellow)"/><text x="273" y="204">$16.20</text><text x="273" y="214">per hour</text>
      <circle cx="305" cy="245" r="20" fill="var(--yellow)"/><text x="305" y="244">$16.20</text><text x="305" y="254">per hour</text>
      <circle cx="498" cy="43" r="30" fill="var(--yellow)"/>
      <text x="498" y="41" font-size="16">$27.00</text><text x="498" y="56" font-size="16">per hour</text>
    </g>

    <circle class="area-chip" cx="364" cy="182" r="24" fill="var(--tan)"/>
    <text class="caps" x="364" y="189" font-size="20" fill="var(--white)" text-anchor="middle">13M2</text>

    <g class="arrows" stroke="var(--yellow)" stroke-width="2.5" fill="none">
      <polyline points="404,128 386,160 436,176"/>
      <polyline points="310,220 340,210 352,236"/>
    </g>
    <g fill="var(--yellow)">
      <polygon points="438,176 426,169 428,181"/>
      <polygon points="354,242 346,230 358,230"/>
    </g>

    <g class="display" fill="var(--white)" font-style="italic" font-size="23" text-anchor="middle">
      <text x="468" y="174">$27.00</text><text x="460" y="198">per hour</text>
      <text x="387" y="265">$97.20</text><text x="379" y="289">per hour</text>
    </g>

    <rect class="question-band" x="0" y="388" width="450" height="127" fill="var(--yellow)"/>
    <text class="caps" font-size="36" fill="var(--white)">
      <tspan x="40" y="430">Why make biking</tspan><tspan x="40" y="467">customers and their $$$</tspan><tspan x="40" y="504">welcome at your business?</tspan>
    </text>

    <circle class="photo-ring" cx="520" cy="400" r="146" fill="var(--green)"/>
    <circle class="photo photo--walker" cx="520" cy="400" r="140" fill="url(#harbour-tone)" role="img" aria-label="Photo of a young man walking his bike along a harbour waterfront"/>

    <text class="body" font-size="19" fill="var(--white)" text-anchor="middle" font-weight="500">
      <tspan x="296" y="566">A Melbourne study showed swapping a car park for six bike parks</tspan>
      <tspan x="296" y="592">could increase the space's retail spend from $27 to $97.20 an hour.</tspan>
      <tspan x="296" y="626">Just think – every bike parked by someone else's business could</tspan>
      <tspan x="296" y="652">have been your customer.</tspan>
    </text>

    <polygon class="slant-rule" points="0,700 592,654 592,664 0,710" fill="var(--green)"/>
    <polygon class="photo photo--sunset" points="0,710 592,664 592,872 0,872" fill="url(#sunset-tone)" role="img" aria-label="Photo of a bicycle silhouetted against a sunset in long grass"/>

    <g class="sticker">
      <rect x="42" y="698" width="79" height="117" rx="4" fill="var(--white)"/>
      <text class="brand" x="81" y="752" font-size="15" fill="var(--green)" text-anchor="middle">Pedal</text>
      <text class="brand" x="81" y="770" font-size="15" fill="var(--green)" text-anchor="middle">Haven</text>
    </g>

    <text class="brand cta" x="296" y="850" font-size="14" fill="var(--white)" text-anchor="middle">See pedalhaven.org.nz to see how you can become a Pedal Haven Business</text>
  </g>
</svg>

</body>
</html>
```